Landscape design build company door flyer

I would like this flyer to convey a high-level of professionalism for a company that is excellent with communication with their clients as well as a company that does incredible installations

Went on vacation/holiday

```html
<!DOCTYPE html>
<html lang="en">
<head>
<meta charset="utf-8">
<title>Cedarline Builders – Door Hanger</title>
<link href="https://fonts.googleapis.com/css2?family=Montserrat:wght@500;600;700&family=Raleway:wght@200&family=Roboto:ital,wght@0,400;0,500;0,700;1,400;1,700&display=swap" rel="stylesheet">
<style>
  :root{
    --backdrop:#466a7d;
    --paper:#ffffff;
    --paper-soft:#f1f2f4;
    --navy:#0f3342;
    --ink:#0f3342;
    --rule:#8a9aa3;
    --white:#ffffff;
  }
  *{margin:0;padding:0;box-sizing:border-box}
  html,body{width:1108px;height:1200px;overflow:hidden}
  body{background:var(--backdrop);position:relative;font-family:'Roboto',Arial,sans-serif}

  .hanger-wrap{
    position:absolute;left:337px;top:38px;
    width:622px;height:1607px;
    transform:scale(0.7);transform-origin:0 0;
    filter:drop-shadow(0 18px 22px rgba(0,0,0,.25));
  }
  .hanger{
    position:absolute;inset:0;
    background:linear-gradient(180deg,var(--paper) 0%,var(--paper-soft) 60%,var(--paper) 100%);
    clip-path:path('M0,311 A311,311 0 0 1 622,311 L622,377 L529,377 A215,215 0 1 0 316,552 L522,552 A100,100 0 0 1 622,652 L622,1567 A40,40 0 0 1 582,1607 L40,1607 A40,40 0 0 1 0,1567 Z');
  }

  .brand{position:absolute;left:0;top:610px;width:345px;text-align:center;color:var(--ink)}
  .brand-mark{display:inline-block;width:16px;height:16px;background:var(--ink);vertical-align:middle;margin-right:8px}
  .brand-name{font-family:'Montserrat',Arial,sans-serif;font-weight:700;font-size:21px;letter-spacing:.5px;vertical-align:middle}
  .brand-tag{display:block;font-family:'Montserrat',Arial,sans-serif;font-weight:700;font-size:9px;letter-spacing:.3px;margin-top:4px}

  .info-panel{position:absolute;left:0;top:716px;width:345px;height:640px;background:var(--navy);color:var(--white)}
  .headline-kicker{position:absolute;left:38px;top:32px;font-weight:700;font-size:28px;letter-spacing:.3px}
  .headline-light{position:absolute;left:36px;top:62px;font-family:'Raleway',Arial,sans-serif;font-weight:200;font-size:62px;line-height:1}
  .headline-bold{position:absolute;left:38px;top:120px;font-weight:700;font-size:51px;line-height:1}
  .tagline{position:absolute;left:38px;top:186px;font-weight:500;font-size:23px}
  .intro{position:absolute;left:38px;top:220px;width:270px;font-size:10.5px;line-height:16.5px;opacity:.9}

  .feature{position:absolute;left:36px;width:290px;height:90px}
  .feature-icon{position:absolute;left:0;top:0;width:58px;height:66px}
  .feature-text{position:absolute;left:68px;top:-32px;width:220px;font-style:italic;font-size:13px;line-height:17px}
  .feature-text b{font-weight:700}
  .feature--1{top:350px}
  .feature--2{top:447px}
  .feature--3{top:544px}

  .photo-panel{position:absolute;left:345px;top:552px;width:277px;height:804px;
    background:linear-gradient(165deg,#1d2a31 0%,#2f3a3e 35%,#4a5b60 60%,#5d93b0 85%,#3f7a98 100%)}

  .cta{position:absolute;left:0;top:1384px;width:622px;text-align:center;color:var(--ink)}
  .cta-label{font-family:'Montserrat',Arial,sans-serif;font-weight:600;font-size:21px;letter-spacing:2px}
  .cta-phone{font-family:'Montserrat',Arial,sans-serif;font-weight:700;font-size:62px;letter-spacing:1px;line-height:1;margin-top:14px}
  .web-line{position:absolute;left:0;top:1490px;width:622px;height:20px;display:flex;align-items:center}
  .web-line::before,.web-line::after{content:"";flex:1;height:1px;background:var(--rule)}
  .web-line span{font-family:'Montserrat',Arial,sans-serif;font-weight:500;font-size:15px;letter-spacing:4.5px;color:var(--ink);padding:0 6px}
  .social{position:absolute;left:0;top:1537px;width:622px;display:flex;justify-content:center;gap:36px}
  .social span{width:26px;height:26px;border-radius:50%;background:var(--ink)}
</style>
</head>
<body>
  <div class="hanger-wrap">
    <div class="hanger">
      <div class="brand">
        <span class="brand-mark"></span><span class="brand-name">CEDARLINE BUILDERS</span>
        <span class="brand-tag">OUTDOOR LIVING SPACES</span>
      </div>

      <div class="info-panel">
        <div class="headline-kicker">HEADLINE</div>
        <div class="headline-light">BUSINESS</div>
        <div class="headline-bold">FLYER TITLE</div>
        <div class="tagline">We Are The Best Team</div>
        <p class="intro">Vivamus est neque, eleifend vel diam vehicula, posuere accumsan ante. Interdum et malesuada fames ac ante ipsum primis in faucibus. Ut porta tincidunt nisi.</p>

        <div class="feature feature--1">
          <svg class="feature-icon" viewBox="0 0 58 66" aria-hidden="true">
            <polygon points="29,2 55,17 55,49 29,64 3,49 3,17" fill="none" stroke="#fff" stroke-width="1.5"/>
            <circle cx="29" cy="33" r="10" fill="none" stroke="#fff" stroke-width="6" stroke-dasharray="4 3.2"/>
            <circle cx="29" cy="33" r="8" fill="#fff"/>
            <circle cx="29" cy="33" r="4" fill="var(--navy)"/>
          </svg>
          <p class="feature-text"><b>Dolor sit amet, consectetur adipiscing elit.</b> Vivamus est neque, eleifend vel diam vehicula, posuere accumsan ante.</p>
        </div>
        <div class="feature feature--2">
          <svg class="feature-icon" viewBox="0 0 58 66" aria-hidden="true">
            <polygon points="29,2 55,17 55,49 29,64 3,49 3,17" fill="none" stroke="#fff" stroke-width="1.5"/>
            <circle cx="32" cy="30" r="9" fill="none" stroke="#fff" stroke-width="2.5"/>
            <line x1="25.5" y1="36.5" x2="18" y2="44" stroke="#fff" stroke-width="3" stroke-linecap="round"/>
          </svg>
          <p class="feature-text"><b>Dolor sit amet, consectetur adipiscing elit.</b> Vivamus est neque, eleifend vel diam vehicula, posuere accumsan ante.</p>
        </div>
        <div class="feature feature--3">
          <svg class="feature-icon" viewBox="0 0 58 66" aria-hidden="true">
            <polygon points="29,2 55,17 55,49 29,64 3,49 3,17" fill="none" stroke="#fff" stroke-width="1.5"/>
            <path d="M29,46 C22,38 19,33 19,28 A10,10 0 0 1 39,28 C39,33 36,38 29,46 Z" fill="none" stroke="#fff" stroke-width="2.5" stroke-linejoin="round"/>
            <circle cx="29" cy="28" r="3.5" fill="#fff"/>
          </svg>
          <p class="feature-text"><b>Dolor sit amet, consectetur adipiscing elit.</b> Interdum et malesuada fames ac ante ipsum primis in faucibus. Ut porta tincidunt nisi.</p>
        </div>
      </div>

      <div class="photo-panel" role="img" aria-label="Photo of a modern building under construction with glass facade and concrete balconies"></div>

      <div class="cta">
        <div class="cta-label">CALL US TODAY!</div>
        <div class="cta-phone">000 123 456</div>
      </div>
      <div class="web-line"><span>www.cedarlinebuilders.com</span></div>
      <div class="social" aria-label="Social media"><span></span><span></span><span></span></div>
    </div>
  </div>
</body>
</html>
```